Birchfield Dental Care Stationery

create stationery, business cards and envelops for business. Use current logo on website but open to new fonts for the business name. Business name is Birchfield Dental Care, would like below the name added "Cosmetic - Family - Implants" Website is www.birchfielddentalcareQX.example. I would like to have modern look, clean, and professional. The water mark of the logo is a great thing to ad as well.

Target Market(s)

General public, Families, Cosmetic, Implant

Industry/Entity Type

Dental

Font styles to use
Sans Serif

Colors
9bcb3c
000000
757575
c9c9c9

Requirements
Must have
• Would like to see different versions of the current logo. Improvements, color, sytle, and class.
Nice to have
• current font has double "oo" in the Birchfield logo, does not need to have with new logo.

```html
<!DOCTYPE html>
<html lang="en">
<head>
<meta charset="utf-8">
<title>Birchfield Dental Care Stationery</title>
<link rel="stylesheet" href="https://fonts.googleapis.com/css2?family=Arimo:wght@400;700&display=swap">
<style>
  :root {
    --bg: #e6ecea;
    --paper: #ffffff;
    --green: #7ad61c;
    --green-soft: #eef8e0;
    --slate: #5a6262;
    --ink: #3c3c3c;
    --shadow: 0 6px 18px rgba(40, 60, 55, 0.18);
  }
  * { box-sizing: border-box; margin: 0; padding: 0; }
  html, body { width: 1200px; height: 1120px; overflow: hidden; }
  body { background: var(--bg); font-family: "Arimo", Arial, sans-serif; color: var(--ink); position: relative; }

  .sheet { position: absolute; background: var(--paper); box-shadow: var(--shadow); overflow: hidden; }

  /* wordmark */
  .brand { display: flex; align-items: center; gap: 8px; }
  .brand-dot { border-radius: 50%; background: var(--green); flex: none; }
  .brand-text { line-height: 1; }
  .brand-name { color: var(--green); font-weight: 700; letter-spacing: 0.02em; white-space: nowrap; }
  .brand-tag { color: var(--ink); font-size: 0.5em; letter-spacing: 0.08em; text-transform: uppercase; margin-top: 4px; white-space: nowrap; }

  /* contact line */
  .contact { position: absolute; display: flex; align-items: center; gap: 6px; color: var(--green); white-space: nowrap; }
  .contact svg { flex: none; fill: var(--green); }

  /* envelope */
  .envelope { left: 40px; top: 60px; width: 560px; height: 300px; }
  .envelope .brand { position: absolute; left: 28px; top: 26px; font-size: 19px; }
  .envelope .band-green { position: absolute; left: 0; top: 108px; width: 380px; height: 30px; background: var(--green); }
  .envelope .band-slate { position: absolute; left: 380px; top: 112px; width: 180px; height: 22px; background: var(--slate); }
  .envelope .contact { bottom: 26px; font-size: 12px; }

  /* letterhead */
  .letterhead { left: 640px; top: 60px; width: 520px; height: 735px; }
  .letterhead .brand { position: absolute; left: 50%; top: 52px; transform: translateX(-50%); font-size: 22px; }
  .watermark { position: absolute; left: 110px; top: 210px; width: 300px; height: 300px; border-radius: 50%; background: var(--green-soft); }
  .letterhead .contact { bottom: 36px; font-size: 12px; }

  /* business cards */
  .card { width: 420px; height: 240px; left: 40px; }
  .card-front { top: 400px; }
  .card-front .brand { position: absolute; left: 50%; top: 50%; transform: translate(-50%, -50%); font-size: 24px; }

  .card-back { top: 680px; }
  .card-back .band-green { position: absolute; left: 0; top: 30px; width: 190px; height: 50px; background: var(--green); color: #fff; padding: 9px 16px; }
  .card-back .holder { font-size: 14px; font-weight: 700; }
  .card-back .role { font-size: 9px; margin-top: 3px; }
  .card-back .band-slate { position: absolute; left: 190px; top: 40px; width: 230px; height: 30px; background: var(--slate); }
  .card-back .brand { position: absolute; left: 22px; top: 128px; font-size: 17px; }
  .card-back .details { position: absolute; left: 250px; top: 118px; list-style: none; font-size: 10px; color: var(--ink); line-height: 1.6; }
  .card-back .details li { display: flex; align-items: flex-start; gap: 6px; }
  .card-back .details svg { fill: var(--green); margin-top: 2px; flex: none; }
</style>
</head>
<body>

<svg width="0" height="0" style="position:absolute">
  <symbol id="icon-pin" viewBox="0 0 12 16"><path d="M6 0a6 6 0 0 0-6 6c0 4.5 6 10 6 10s6-5.5 6-10a6 6 0 0 0-6-6zm0 8.5A2.5 2.5 0 1 1 6 3.5a2.5 2.5 0 0 1 0 5z"/></symbol>
  <symbol id="icon-fax" viewBox="0 0 16 14"><path d="M4 0h8v4H4zM1 5h14a1 1 0 0 1 1 1v5h-3v3H3v-3H0V6a1 1 0 0 1 1-1zm4 5v3h6v-3z"/></symbol>
  <symbol id="icon-phone" viewBox="0 0 10 16"><path d="M2 0h6a2 2 0 0 1 2 2v12a2 2 0 0 1-2 2H2a2 2 0 0 1-2-2V2a2 2 0 0 1 2-2zm0 2v10h6V2zm3 11a1 1 0 1 0 0 2 1 1 0 0 0 0-2z"/></symbol>
</svg>

<!-- Envelope -->
<section class="sheet envelope" aria-label="Envelope">
  <div class="brand">
    <span class="brand-dot" style="width:26px;height:26px"></span>
    <div class="brand-text">
      <div class="brand-name">Birchfield Dental Care</div>
      <div class="brand-tag">Cosmetic - Family - Implants</div>
    </div>
  </div>
  <div class="band-green"></div>
  <div class="band-slate"></div>
  <div class="contact" style="left:28px"><svg width="10" height="13"><use href="#icon-pin"/></svg>1820 North Alder Lane Fernvale, QX 40517</div>
  <div class="contact" style="left:330px"><svg width="12" height="11"><use href="#icon-fax"/></svg>(555) 014-2290</div>
  <div class="contact" style="left:450px"><svg width="8" height="13"><use href="#icon-phone"/></svg>(555) 014-7731</div>
</section>

<!-- Letterhead -->
<section class="sheet letterhead" aria-label="Letterhead">
  <div class="brand">
    <span class="brand-dot" style="width:30px;height:30px"></span>
    <div class="brand-text">
      <div class="brand-name">Birchfield Dental Care</div>
      <div class="brand-tag">Cosmetic - Family - Implants</div>
    </div>
  </div>
  <div class="watermark" role="img" aria-label="Faint watermark of the practice logo"></div>
  <div class="contact" style="left:34px"><svg width="10" height="13"><use href="#icon-pin"/></svg>1820 North Alder Lane Fernvale, QX 40517</div>
  <div class="contact" style="left:300px"><svg width="12" height="11"><use href="#icon-fax"/></svg>(555) 014-2290</div>
  <div class="contact" style="left:410px"><svg width="8" height="13"><use href="#icon-phone"/></svg>(555) 014-7731</div>
</section>

<!-- Business card front -->
<section class="sheet card card-front" aria-label="Business card front">
  <div class="brand">
    <span class="brand-dot" style="width:30px;height:30px"></span>
    <div class="brand-text">
      <div class="brand-name">Birchfield Dental Care</div>
      <div class="brand-tag">Cosmetic - Family - Implants</div>
    </div>
  </div>
</section>

<!-- Business card back -->
<section class="sheet card card-back" aria-label="Business card back">
  <div class="band-green">
    <div class="holder">Dr. Miriam Castell</div>
    <div class="role">Fernvale, QX Dentist</div>
  </div>
  <div class="band-slate"></div>
  <div class="brand">
    <span class="brand-dot" style="width:22px;height:22px"></span>
    <div class="brand-text">
      <div class="brand-name">Birchfield Dental Care</div>
      <div class="brand-tag">Cosmetic - Family - Implants</div>
    </div>
  </div>
  <ul class="details">
    <li><svg width="7" height="11"><use href="#icon-phone"/></svg>(555) 014-7731</li>
    <li><svg width="10" height="9"><use href="#icon-fax"/></svg>(555) 014-2290</li>
    <li><svg width="8" height="11"><use href="#icon-pin"/></svg><span>1820 North Alder Lane<br>Fernvale, QX 40517</span></li>
  </ul>
</section>

</body>
</html>
```